Need UI design for an iOS app game with most of the layout planned

The name of the game is "QUADRIX".

The goal of the game is to find a way to manipulate four numbers so that the end result is 24. Addition, subtraction, multiplication and division may be used and each number can only be used once.

The list of items we need is:

1. launch image, app icon, UI design of all scenes (10-12 scenes) of the app.
2. App background image should support screen size of both 640x1136.
3. Files are preferred to be in (.eps) format so that resolution can be adjusted later. But other file formats are welcome as long as resolution is high enough.
4. Icons, buttons, background image etc. should have their own file so that later they can be moved around in case design is changed.

The detailed requirement is in the attached file. The actual layout can vary if it can help achieve better result. We also attached several screenshots from iOS game "Glimtor". You can use that as your reference.

```html
<!DOCTYPE html>
<html lang="en">
<head>
<meta charset="utf-8">
<title>QUADRIX – Game UI Screens</title>
<link rel="stylesheet" href="https://fonts.googleapis.com/css2?family=Bangers&display=swap">
<style>
  :root {
    --canvas-bg: #f2f2f2;
    --field-light: #c8e460;
    --field-mid: #95cb3c;
    --field-dark: #5ea62a;
    --header-yellow: #fff200;
    --ink: #111111;
    --blue-top: #2a8fe0;
    --blue-bottom: #0a56a8;
    --orange-top: #ff9a2a;
    --orange-bottom: #ff5a00;
    --button-rim: #ffe95a;
    --tile-green: #0d4d16;
    --tile-locked: #0b2a10;
    --tile-rim: #c9d84a;
    --tile-rim-locked: #4d6a22;
    --accent-yellow: #ffee00;
    --white: #ffffff;
  }
  * { box-sizing: border-box; margin: 0; padding: 0; }
  html, body { width: 1200px; height: 1200px; overflow: hidden; }
  body {
    background: var(--canvas-bg);
    font-family: "Bangers", "Impact", sans-serif;
    color: var(--ink);
  }
  .board {
    position: relative;
    width: 1200px; height: 1200px;
    display: flex; justify-content: center; align-items: center; gap: 40px;
  }
  .screen {
    position: relative;
    width: 340px; height: 604px;
    overflow: hidden;
    background: radial-gradient(ellipse 75% 60% at 50% 45%, var(--field-light) 0%, var(--field-mid) 55%, var(--field-dark) 100%);
    box-shadow: 0 6px 24px rgba(0,0,0,.18);
  }

  /* shared buttons */
  .icon-button {
    position: absolute; top: 6px;
    width: 57px; height: 57px;
    background: var(--tile-green);
    border: 2px solid var(--tile-rim);
    border-radius: 4px;
    display: flex; align-items: center; justify-content: center;
    color: var(--accent-yellow);
  }
  .icon-button--settings { left: 6px; }
  .icon-button--info { right: 6px; font-family: Georgia, serif; font-style: italic; font-size: 30px; }

  .pill {
    position: absolute; left: 50%; transform: translateX(-50%);
    display: flex; align-items: center; justify-content: center;
    color: var(--white);
    letter-spacing: 1px;
    border: 2px solid var(--button-rim);
    border-radius: 4px;
    text-shadow: 0 1px 0 rgba(0,0,0,.25);
  }
  .pill--blue { background: linear-gradient(var(--blue-top), var(--blue-bottom)); }
  .pill--orange { background: linear-gradient(var(--orange-top), var(--orange-bottom)); }

  /* home */
  .home-logo {
    position: absolute; left: 0; right: 0; top: 200px;
    display: flex; align-items: center; justify-content: center; gap: 12px;
  }
  .home-logo__mark { width: 34px; height: 34px; border-radius: 50%; background: var(--orange-bottom); }
  .home-logo__name { font-size: 62px; color: var(--orange-bottom); letter-spacing: 2px; }
  .home-button { width: 264px; height: 58px; font-size: 22px; }
  .home-button--single { top: 412px; }
  .home-button--multi { top: 480px; }

  /* header bar */
  .top-bar {
    position: absolute; left: 0; top: 0; width: 100%; height: 64px;
    background: var(--header-yellow);
  }
  .top-bar::after {
    content: ""; position: absolute; left: 0; right: 0; bottom: -6px; height: 6px;
    background: radial-gradient(circle at 4px 0, var(--header-yellow) 4px, transparent 4.5px) 0 0 / 8px 6px repeat-x;
  }
  .back-button {
    position: absolute; left: 6px; top: 6px;
    width: 92px; height: 54px;
    background: linear-gradient(var(--blue-top), var(--blue-bottom));
    border: 2px solid #0a3f80; border-radius: 4px;
    display: flex; align-items: center; justify-content: center;
  }
  .brand-name { font-size: 22px; color: var(--orange-bottom); letter-spacing: 1px; }
  .top-bar .brand-name { position: absolute; top: 18px; }
  .modes .brand-name { left: 50%; transform: translateX(-50%); }
  .levels .brand-name { right: 8px; }
  .coin-panel {
    position: absolute; right: 6px; top: 6px;
    width: 90px; height: 54px;
    background: linear-gradient(var(--blue-top), var(--blue-bottom));
    border: 2px solid #0a3f80; border-radius: 4px;
    color: var(--white);
    display: grid; grid-template-columns: 22px 1fr; align-items: center; padding: 4px 8px; font-size: 13px; line-height: 1.1;
  }
  .coin-panel__coin { width: 16px; height: 16px; border-radius: 50%; background: #f5c200; border: 2px solid #d49a00; }
  .coin-panel__value { grid-column: 1 / 3; text-align: center; font-size: 14px; }
  .heading-title {
    position: absolute; left: 108px; top: 8px;
    font-size: 24px; line-height: 1; letter-spacing: 1px;
  }

  /* modes */
  .mode-copy {
    position: absolute; left: 40px; right: 40px;
    text-align: center; font-size: 11px; line-height: 1.75; letter-spacing: .6px;
  }
  .mode-button { width: 196px; height: 44px; font-size: 21px; }

  /* levels */
  .level-grid {
    position: absolute; left: 5px; right: 5px; top: 97px;
    display: grid; grid-template-columns: repeat(3, 94px); justify-content: space-between; row-gap: 36px;
  }
  .level-grid::after {
    content: ""; position: absolute; left: -5px; right: -5px; top: 430px; height: 100px;
    background: linear-gradient(rgba(95,166,42,0), var(--field-dark) 70%);
  }
  .level-tile {
    position: relative; width: 94px; height: 101px;
    border-radius: 4px; overflow: hidden;
    display: flex; flex-direction: column; align-items: center; justify-content: center; gap: 8px;
  }
  .level-tile--open { background: var(--tile-green); border: 2px solid var(--tile-rim); color: var(--accent-yellow); font-size: 13px; }
  .level-tile--locked { background: var(--tile-locked); border: 2px solid var(--tile-rim-locked); }
  .level-tile__stars { display: flex; gap: 4px; }
  .level-tile__lock { position: absolute; opacity: .35; }
  .level-tile__label {
    position: relative; color: var(--accent-yellow); font-size: 24px; letter-spacing: 1px;
    transform: rotate(-40deg); text-shadow: 0 2px 0 #2a2a00;
  }
</style>
</head>
<body>
<main class="board">

  <!-- Home screen -->
  <section class="screen home" aria-label="Home screen">
    <div class="icon-button icon-button--settings" aria-label="Settings">
      <svg width="30" height="30" viewBox="0 0 24 24" fill="none" stroke="currentColor" stroke-width="2">
        <circle cx="9" cy="9" r="3"/>
        <path d="M9 2v3M9 13v3M2 9h3M13 9h3M4 4l2 2M12 12l2 2M4 14l2-2M12 6l2-2"/>
        <circle cx="18" cy="18" r="2"/>
      </svg>
    </div>
    <div class="icon-button icon-button--info" aria-label="Info">i</div>

    <div class="home-logo">
      <span class="home-logo__mark"></span>
      <span class="home-logo__name">QUADRIX</span>
    </div>

    <div class="pill pill--blue home-button home-button--single">SINGLE PLAYER</div>
    <div class="pill pill--orange home-button home-button--multi">MULTI PLAYER</div>
  </section>

  <!-- Mode select screen -->
  <section class="screen modes" aria-label="Mode select screen">
    <header class="top-bar">
      <div class="back-button" aria-label="Back">
        <svg width="48" height="26" viewBox="0 0 48 26"><path d="M2 13 L18 2 V8 H44 V18 H18 V24 Z" fill="#fff"/></svg>
      </div>
      <span class="brand-name">QUADRIX</span>
      <div class="coin-panel">
        <span class="coin-panel__coin"></span><span>COINS</span>
        <span class="coin-panel__value">1268</span>
      </div>
    </header>

    <p class="mode-copy" style="top:124px">PROIN GRAVIDA NIBH VEL VELIT AUCTOR ALIQUET. AENEAN SOLLICITUDIN, LOREM QUIS.</p>
    <div class="pill pill--orange mode-button" style="top:190px">MODE 1</div>

    <p class="mode-copy" style="top:295px">PROIN GRAVIDA NIBH VEL VELIT AUCTOR ALIQUET.</p>
    <div class="pill pill--orange mode-button" style="top:360px">MODE 2</div>

    <p class="mode-copy" style="top:465px">PROIN GRAVIDA NIBH VEL VELIT AUCTOR ALIQUET. AENEAN SOLLICITUDIN, LOREM QUIS.</p>
    <div class="pill pill--orange mode-button" style="top:531px">MODE 3</div>
  </section>

  <!-- Level select screen -->
  <section class="screen levels" aria-label="Level select screen">
    <header class="top-bar">
      <div class="back-button" aria-label="Back">
        <svg width="48" height="26" viewBox="0 0 48 26"><path d="M2 13 L18 2 V8 H44 V18 H18 V24 Z" fill="#fff"/></svg>
      </div>
      <h1 class="heading-title">HEADING<br>TITLE</h1>
      <span class="brand-name">QUADRIX</span>
    </header>

    <div class="level-grid">
      <div class="level-tile level-tile--open">
        <span>LEVEL 1</span>
        <span class="level-tile__stars">
          <svg width="18" height="18" viewBox="0 0 24 24"><path d="M12 2l3 7h7l-5.5 4.5 2 7.5L12 17l-6.5 4 2-7.5L2 9h7z" fill="#ffee00"/></svg>
          <svg width="18" height="18" viewBox="0 0 24 24"><path d="M12 2l3 7h7l-5.5 4.5 2 7.5L12 17l-6.5 4 2-7.5L2 9h7z" fill="#ffee00"/></svg>
          <svg width="18" height="18" viewBox="0 0 24 24"><path d="M12 2l3 7h7l-5.5 4.5 2 7.5L12 17l-6.5 4 2-7.5L2 9h7z" fill="none" stroke="#ffee00" stroke-width="1.6"/></svg>
        </span>
      </div>
      <div class="level-tile level-tile--open">
        <span>LEVEL 2</span>
        <span class="level-tile__stars">
          <svg width="18" height="18" viewBox="0 0 24 24"><path d="M12 2l3 7h7l-5.5 4.5 2 7.5L12 17l-6.5 4 2-7.5L2 9h7z" fill="#ffee00"/></svg>
          <svg width="18" height="18" viewBox="0 0 24 24"><path d="M12 2l3 7h7l-5.5 4.5 2 7.5L12 17l-6.5 4 2-7.5L2 9h7z" fill="#ffee00"/></svg>
          <svg width="18" height="18" viewBox="0 0 24 24"><path d="M12 2l3 7h7l-5.5 4.5 2 7.5L12 17l-6.5 4 2-7.5L2 9h7z" fill="none" stroke="#ffee00" stroke-width="1.6"/></svg>
        </span>
      </div>
      <div class="level-tile level-tile--locked"><svg class="level-tile__lock" width="44" height="50" viewBox="0 0 44 50" fill="none" stroke="#c9d84a" stroke-width="3"><path d="M10 22V14a12 12 0 0 1 24 0v8"/><rect x="4" y="22" width="36" height="26" rx="3"/></svg><span class="level-tile__label">LOCKED</span></div>
      <div class="level-tile level-tile--locked"><svg class="level-tile__lock" width="44" height="50" viewBox="0 0 44 50" fill="none" stroke="#c9d84a" stroke-width="3"><path d="M10 22V14a12 12 0 0 1 24 0v8"/><rect x="4" y="22" width="36" height="26" rx="3"/></svg><span class="level-tile__label">LOCKED</span></div>
      <div class="level-tile level-tile--locked"><svg class="level-tile__lock" width="44" height="50" viewBox="0 0 44 50" fill="none" stroke="#c9d84a" stroke-width="3"><path d="M10 22V14a12 12 0 0 1 24 0v8"/><rect x="4" y="22" width="36" height="26" rx="3"/></svg><span class="level-tile__label">LOCKED</span></div>
      <div class="level-tile level-tile--locked"><svg class="level-tile__lock" width="44" height="50" viewBox="0 0 44 50" fill="none" stroke="#c9d84a" stroke-width="3"><path d="M10 22V14a12 12 0 0 1 24 0v8"/><rect x="4" y="22" width="36" height="26" rx="3"/></svg><span class="level-tile__label">LOCKED</span></div>
      <div class="level-tile level-tile--locked"><svg class="level-tile__lock" width="44" height="50" viewBox="0 0 44 50" fill="none" stroke="#c9d84a" stroke-width="3"><path d="M10 22V14a12 12 0 0 1 24 0v8"/><rect x="4" y="22" width="36" height="26" rx="3"/></svg><span class="level-tile__label">LOCKED</span></div>
      <div class="level-tile level-tile--locked"><svg class="level-tile__lock" width="44" height="50" viewBox="0 0 44 50" fill="none" stroke="#c9d84a" stroke-width="3"><path d="M10 22V14a12 12 0 0 1 24 0v8"/><rect x="4" y="22" width="36" height="26" rx="3"/></svg><span class="level-tile__label">LOCKED</span></div>
      <div class="level-tile level-tile--locked"><svg class="level-tile__lock" width="44" height="50" viewBox="0 0 44 50" fill="none" stroke="#c9d84a" stroke-width="3"><path d="M10 22V14a12 12 0 0 1 24 0v8"/><rect x="4" y="22" width="36" height="26" rx="3"/></svg><span class="level-tile__label">LOCKED</span></div>
      <div class="level-tile level-tile--locked"><svg class="level-tile__lock" width="44" height="50" viewBox="0 0 44 50" fill="none" stroke="#c9d84a" stroke-width="3"><path d="M10 22V14a12 12 0 0 1 24 0v8"/><rect x="4" y="22" width="36" height="26" rx="3"/></svg><span class="level-tile__label">LOCKED</span></div>
      <div class="level-tile level-tile--locked"><svg class="level-tile__lock" width="44" height="50" viewBox="0 0 44 50" fill="none" stroke="#c9d84a" stroke-width="3"><path d="M10 22V14a12 12 0 0 1 24 0v8"/><rect x="4" y="22" width="36" height="26" rx="3"/></svg><span class="level-tile__label">LOCKED</span></div>
      <div class="level-tile level-tile--locked"><svg class="level-tile__lock" width="44" height="50" viewBox="0 0 44 50" fill="none" stroke="#c9d84a" stroke-width="3"><path d="M10 22V14a12 12 0 0 1 24 0v8"/><rect x="4" y="22" width="36" height="26" rx="3"/></svg><span class="level-tile__label">LOCKED</span></div>
    </div>
  </section>

</main>
</body>
</html>
```